Poster for our band

We need a logo and poster designing for us to send to the venues we are performing at. Our band is called "Quarry"
Can use different backgrounds to make poster look more Arty
We would like the poster to look contemporary, modern and unique. As many or as little pictures can be used that I will send.
We perform at Holiday Parks, Hotels etc so the Poster needs to look classy and sophisticated.Can be Portrait or Landscape. Poster could be Black and White or Colour
A very creative Logo
Could contain the following script somewhere on the poster.

Performing hits by- The Drifters Bay, Silver Lantern, Bright Oar, Darren Pollock, Moths of Varney, Gulls, Q9, Marble Poets and many more.

Poster needs our website address.
www.thebandquarry-example.co.uk

Poster needs our Agent Name and number

Represented by- RZK - 01632 960418

Target Market(s)

Holiday Parks
Hotels
Nightclubs
Bars

Industry/Entity Type

Colors
000000

Requirements
Must have
• Can be Portrait or Landscape. Poster could be Black and White or Colour
A very creative Logo

www.thebandquarry-example.co.uk

Nice to have
• Cool, Contemopoary, Modern design
Photos can be cut out or changed in anyway to make us look great.

```html
<!DOCTYPE html>
<html lang="en">
<head>
<meta charset="utf-8">
<title>Quarry – Band Poster</title>
<link rel="stylesheet" href="https://fonts.googleapis.com/css2?family=Roboto+Condensed:wght@300&display=swap">
<style>
  :root {
    --ink-black: #000000;
    --night-brown: #1d1108;
    --glow-amber: #5a3510;
    --lamp-orange: #6b3a0c;
    --text-white: #ffffff;
  }
  html, body {
    margin: 0;
    padding: 0;
    width: 802px;
    height: 1200px;
    overflow: hidden;
    background: var(--ink-black);
  }
  .poster {
    position: relative;
    width: 802px;
    height: 1200px;
    overflow: hidden;
    background: var(--ink-black);
    font-family: "Roboto Condensed", "Arial Narrow", sans-serif;
    font-weight: 300;
    color: var(--text-white);
  }
  .poster__backdrop {
    position: absolute;
    inset: 0;
    background:
      radial-gradient(ellipse 14% 10% at 58% 20%, var(--lamp-orange) 0%, transparent 100%),
      radial-gradient(ellipse 60% 22% at 55% 72%, var(--glow-amber) 0%, var(--night-brown) 45%, transparent 75%),
      linear-gradient(180deg, var(--ink-black) 0%, var(--night-brown) 55%, var(--ink-black) 85%);
  }
  .poster__logo {
    position: absolute;
    left: 0;
    right: 0;
    top: 350px;
    margin: 0;
    text-align: center;
    font-size: 190px;
    line-height: 1;
    font-weight: 300;
    letter-spacing: 2px;
    text-transform: uppercase;
    white-space: nowrap;
    color: var(--text-white);
  }
  .poster__website {
    position: absolute;
    left: 0;
    right: 0;
    top: 1018px;
    margin: 0;
    text-align: center;
    font-size: 40px;
    line-height: 1.2;
    white-space: nowrap;
  }
  .poster__agent {
    position: absolute;
    left: 0;
    right: 0;
    top: 1140px;
    margin: 0;
    text-align: center;
    font-size: 30px;
    line-height: 1.2;
    white-space: nowrap;
  }
</style>
</head>
<body>
  <main class="poster">
    <div class="poster__backdrop" role="img" aria-label="Blurred night-time photograph of a city road with street lamps, motorway signs and streaking car lights"></div>
    <h1 class="poster__logo">Quarry</h1>
    <p class="poster__website">www.thebandquarry-example.co.uk</p>
    <p class="poster__agent">Represented by- RZK - 01632 960418</p>
  </main>
</body>
</html>
```